Energy Drink label Velamo

Design a Label to be used on the packaging label/mock up for a energy drink. The name VELAMO means Black Bull & Bull ( in the 11 languages in the target country we want to launch ). I would like a in your face energy drink label design. Please see uploaded files as reference . Something out of the box thinking. For 500ml tin can label.

Target Market(s)

Population of Africa

Industry/Entity Type

Energy Drink

Colors
EB3D1F
EC4F4E
F09395
F8D3D4
FCEDEE

Requirements
Must have
• Bold and attractive design ( Black , Red , Silver , White ) as MAIN color scheme, as attached files I uploaded
Nice to have
• option of a white background and also black ( matte / carbon fibre effect )

```html
<!DOCTYPE html>
<html lang="en">
<head>
<meta charset="utf-8">
<title>Velamo Energy Drink Label</title>
<link rel="stylesheet" href="https://fonts.googleapis.com/css2?family=Anton&family=Alfa+Slab+One&family=Oswald:wght@500;600&display=swap">
<style>
  :root {
    --stage: #e6e4e4;
    --can-grey: #3b3b3e;
    --can-grey-dark: #2a2a2c;
    --red-deep: #7a1014;
    --red-mid: #a3171c;
    --red-bright: #d3262b;
    --silver: #d9d9dc;
    --white: #ffffff;
  }
  * { box-sizing: border-box; margin: 0; padding: 0; }
  html, body {
    width: 1200px;
    height: 801px;
    overflow: hidden;
    background: var(--stage);
  }
  .stage {
    position: relative;
    width: 1200px;
    height: 801px;
    display: flex;
    align-items: center;
    justify-content: center;
  }
  .label {
    position: relative;
    width: 400px;
    height: 740px;
    background: linear-gradient(90deg, var(--can-grey-dark) 0%, var(--can-grey) 20%, var(--can-grey) 80%, var(--can-grey-dark) 100%);
    overflow: hidden;
  }
  .label__panel {
    position: absolute;
    inset: 0;
  }
  .label__brand {
    position: absolute;
    top: 44px;
    left: 0;
    width: 100%;
    text-align: center;
    font-family: "Anton", sans-serif;
    font-size: 112px;
    line-height: 1;
    letter-spacing: 1px;
    color: var(--white);
  }
  .label__mascot {
    position: absolute;
    top: 200px;
    left: 70px;
    width: 260px;
    height: 300px;
  }
  .label__variant {
    position: absolute;
    top: 528px;
    width: 100%;
    text-align: center;
    font-family: "Oswald", sans-serif;
    font-weight: 500;
    font-size: 26px;
    letter-spacing: 2px;
    color: var(--white);
  }
  .label__type {
    position: absolute;
    top: 572px;
    width: 100%;
    text-align: center;
    font-family: "Alfa Slab One", serif;
    font-size: 34px;
    color: var(--red-bright);
    -webkit-text-stroke: 1.5px var(--white);
    letter-spacing: 1px;
  }
  .label__volume {
    position: absolute;
    top: 640px;
    width: 100%;
    text-align: center;
    font-family: "Oswald", sans-serif;
    font-weight: 600;
    font-size: 28px;
    letter-spacing: 1px;
    color: var(--white);
  }
</style>
</head>
<body>
  <main class="stage">
    <section class="label">
      <svg class="label__panel" viewBox="0 0 400 740" width="400" height="740" aria-hidden="true">
        <defs>
          <linearGradient id="panel-red" x1="0" y1="0" x2="1" y2="0">
            <stop offset="0" stop-color="var(--red-deep)"/>
            <stop offset="0.5" stop-color="var(--red-mid)"/>
            <stop offset="1" stop-color="var(--red-deep)"/>
          </linearGradient>
        </defs>
        <polygon points="200,20 360,200 360,600 200,730 40,600 40,200" fill="url(#panel-red)"/>
        <line x1="30" y1="200" x2="30" y2="600" stroke="var(--silver)" stroke-width="2" opacity="0.7"/>
        <line x1="370" y1="200" x2="370" y2="600" stroke="var(--silver)" stroke-width="2" opacity="0.7"/>
        <polyline points="22,170 200,5 378,170" fill="none" stroke="var(--silver)" stroke-width="2" opacity="0.5"/>
      </svg>
      <h1 class="label__brand">VELAMO</h1>
      <svg class="label__mascot" viewBox="0 0 260 300" role="img" aria-label="Illustration of an angry bull head with red horns inside a shield">
        <defs>
          <radialGradient id="mascot-tone" cx="0.5" cy="0.45" r="0.6">
            <stop offset="0" stop-color="#cfcfd2"/>
            <stop offset="1" stop-color="#6e6e72"/>
          </radialGradient>
        </defs>
        <path d="M20 40 Q130 0 240 40 L230 200 Q130 300 130 300 Q130 300 30 200 Z" fill="url(#mascot-tone)"/>
      </svg>
      <p class="label__variant">ORIGINAL</p>
      <p class="label__type">ENERGY DRINK</p>
      <p class="label__volume">500 ml</p>
    </section>
  </main>
</body>
</html>
```